Farming Operation Business Card

We need a logo designed for a Farming operation. We grow walnuts, harvest walnuts, provide orchard management for customers, lease farm ground, repair farm equipment and prune trees. This is a family owned business with two boys ages 20 & 21 working under their father. I want a design and logo hip enough for the boys but not too crazy for their conservative father. Favorite colors tend to be traditional green, navy blue and grey but not all together and open to al colors.

Let me make my concept clearer - These guys are Ranchers, Cowbolys, true blue collar workers. Up at the crack of dawn, driving a tractor, preparing the earth for harvest. These men work long hours and on big equipment to produce a out of the world walnut. They get down and dirty at their job but know how to clean up and treat a woman right. Farming is their fist love, they know nothing more then digging their hands into God's earth and pouring their sweat and blood into their harvest. Please no more designs with children holding hands in the design.

Target Market(s)

Local walnut farmers

Industry/Entity Type

Farming

Contact Information for Business Card

Callory Farms. Neil Callory. 559-731-4460On back services listed: Walnut Harvesting / Orchard Management / Orchard Leasing / Equipment Repair / Pruning

Font styles to use
Serif

Requirements
Must have
• Callory Farms
Nice to have
• A Walnut... possibly with Callory Farms logo designed in the walnut
Should not have
• NO Squirrels / No children holing hands or pictures of people

```html
<!DOCTYPE html>
<html lang="en">
<head>
<meta charset="utf-8">
<title>Callory Farms Business Card</title>
<link rel="stylesheet" href="https://fonts.googleapis.com/css2?family=Open+Sans:wght@400;600;700&display=swap">
<style>
  :root {
    --page-grey: #d6d6d4;
    --card-navy: #134a5f;
    --card-black: #050505;
    --card-green: #77bc14;
    --text-white: #ffffff;
  }
  * { margin: 0; padding: 0; box-sizing: border-box; }
  html, body {
    width: 1200px;
    height: 900px;
    overflow: hidden;
    background: var(--page-grey);
    font-family: "Open Sans", Arial, sans-serif;
  }
  .card {
    position: absolute;
    left: 250px;
    width: 700px;
    height: 400px;
    overflow: hidden;
    box-shadow: 0 6px 18px rgba(0,0,0,0.18);
  }
  .card-back { top: 40px; }
  .card-front { top: 460px; }
  .card-shapes { position: absolute; inset: 0; display: block; }

  .service-list {
    position: absolute;
    left: 60px;
    top: 92px;
    list-style: none;
    color: var(--text-white);
    font-weight: 600;
    font-size: 19px;
    line-height: 1.3;
  }
  .service-list li { display: flex; align-items: center; }
  .service-list li::before {
    content: "";
    width: 9px; height: 9px;
    border-radius: 50%;
    background: var(--text-white);
    margin-right: 12px;
  }

  .brand-mark {
    position: absolute;
    display: flex;
    align-items: center;
    justify-content: center;
    text-align: center;
  }
  .brand-mark .brand-ring {
    position: absolute;
    border: 6px solid var(--card-green);
    border-radius: 50%;
  }
  .brand-name {
    position: relative;
    color: var(--card-green);
    font-weight: 600;
    text-transform: uppercase;
    letter-spacing: 1px;
  }
  .card-back .brand-mark { left: 440px; top: 90px; width: 240px; height: 220px; }
  .card-back .brand-ring { width: 150px; height: 150px; left: 45px; top: 10px; }
  .card-back .brand-name { font-size: 27px; margin-top: 130px; }

  .card-front .brand-mark { left: 70px; top: 80px; width: 240px; height: 240px; }
  .card-front .brand-ring { width: 220px; height: 220px; left: 10px; top: 10px; }
  .card-front .brand-name { font-size: 26px; line-height: 1.2; }

  .contact-block {
    position: absolute;
    right: 55px;
    top: 140px;
    color: var(--text-white);
    text-align: right;
  }
  .contact-name { font-size: 29px; font-weight: 700; margin-bottom: 22px; }
  .contact-line {
    font-size: 19px;
    line-height: 1.3;
    display: flex;
    justify-content: flex-end;
    align-items: center;
    gap: 9px;
  }
  .contact-line svg { width: 16px; height: 16px; flex: none; }
  .contact-address { font-size: 19px; line-height: 1.25; margin-top: 2px; padding-right: 25px; }
</style>
</head>
<body>

<section class="card card-back" aria-label="Card back, services">
  <svg class="card-shapes" viewBox="0 0 700 400" aria-hidden="true">
    <rect width="700" height="400" fill="var(--card-navy)"/>
    <path d="M470 0 C335 90 300 300 420 400 L700 400 L700 0 Z" fill="var(--card-green)"/>
    <path d="M490 0 C352 95 322 300 436 400 L700 400 L700 0 Z" fill="var(--card-black)"/>
  </svg>
  <ul class="service-list">
    <li>Walnut Harvesting</li>
    <li>Orchard Management</li>
    <li>Orchard Leasing</li>
    <li>Equipment Repair / Pruning</li>
  </ul>
  <div class="brand-mark">
    <span class="brand-ring"></span>
    <span class="brand-name">Callory Farms</span>
  </div>
</section>

<section class="card card-front" aria-label="Card front, contact">
  <svg class="card-shapes" viewBox="0 0 700 400" aria-hidden="true">
    <rect width="700" height="400" fill="var(--card-black)"/>
    <path d="M350 0 C520 110 510 300 250 400 L700 400 L700 0 Z" fill="var(--card-navy)"/>
    <path d="M378 0 C545 115 535 305 285 400 L700 400 L700 0 Z" fill="var(--card-green)"/>
  </svg>
  <div class="brand-mark">
    <span class="brand-ring"></span>
    <span class="brand-name">Callory<br>Farms</span>
  </div>
  <div class="contact-block">
    <p class="contact-name">Neil Callory</p>
    <p class="contact-line">555-208-9137
      <svg viewBox="0 0 24 24" aria-hidden="true"><path fill="#fff" d="M6.6 10.8a15.2 15.2 0 0 0 6.6 6.6l2.2-2.2c.3-.3.7-.4 1-.2 1.1.4 2.3.6 3.6.6.6 0 1 .4 1 1V20c0 .6-.4 1-1 1A17 17 0 0 1 3 4c0-.6.4-1 1-1h3.5c.6 0 1 .4 1 1 0 1.3.2 2.5.6 3.6.1.3 0 .7-.2 1z"/></svg>
    </p>
    <p class="contact-line">www.website.com
      <svg viewBox="0 0 24 24" aria-hidden="true"><circle cx="12" cy="12" r="10" fill="#fff"/><path d="M2 12h20M12 2c3 3 3 17 0 20M12 2c-3 3-3 17 0 20" stroke="var(--card-green)" stroke-width="1.6" fill="none"/></svg>
    </p>
    <p class="contact-address">12345, Address Goes Here<br>Country Name, 123456</p>
  </div>
</section>

</body>
</html>
```